Letterhead creation for military law attorney

I need letterhead design for my business. We are now only doing military law and need to change address, logo and vision. I like the idea of using an eagle or a jolly roger flag

Target Market(s)

Military Law Clients

Colors
3176b5
85abd2

Requirements
Must have
• We are defending people against the government
Nice to have
• Jolly Roger Flag

```html
<!DOCTYPE html>
<html lang="en">
<head>
<meta charset="utf-8">
<title>Harlan Defense, PLLC — Letterhead</title>
<link href="https://fonts.googleapis.com/css2?family=Open+Sans:wght@400;600&display=swap" rel="stylesheet">
<style>
  :root {
    --backdrop: #2e2e2e;
    --paper: #ffffff;
    --ink: #1c1c1c;
    --ink-soft: #3a3a3a;
    --rule: #1c1c1c;
    --signature-tone: #ececec;
  }
  * { box-sizing: border-box; margin: 0; padding: 0; }
  html, body {
    width: 1200px;
    height: 900px;
    overflow: hidden;
    background: var(--backdrop);
    font-family: "Open Sans", sans-serif;
    color: var(--ink);
  }
  .letterhead {
    position: absolute;
    left: 296px;
    top: 20px;
    width: 608px;
    height: 860px;
    background: var(--paper);
    padding: 52px 56px;
  }
  .masthead {
    display: flex;
    justify-content: space-between;
    align-items: flex-end;
    padding-bottom: 10px;
    border-bottom: 1.5px solid var(--rule);
  }
  .brand {
    display: flex;
    align-items: center;
    gap: 12px;
  }
  .brand-mark {
    width: 30px;
    height: 30px;
    border-radius: 50%;
    background: var(--ink);
  }
  .brand-name {
    font-size: 12px;
    font-weight: 400;
    letter-spacing: 0.32em;
    text-transform: uppercase;
  }
  .contact {
    font-size: 7.5px;
    font-style: normal;
    line-height: 1.45;
    color: var(--ink-soft);
  }
  .letter-body {
    margin-top: 64px;
    font-size: 10.5px;
    line-height: 2.1;
    color: var(--ink-soft);
  }
  .letter-date { margin-bottom: 38px; }
  .letter-body p + p { margin-top: 24px; }
  .sign-off {
    width: 120px;
    margin: 28px 10px 0 auto;
    text-align: center;
    font-size: 9.5px;
    line-height: 1.4;
    color: var(--ink-soft);
  }
  .signature {
    height: 40px;
    margin-bottom: 6px;
    background: var(--signature-tone);
    border-radius: 4px;
  }
</style>
</head>
<body>
  <article class="letterhead">
    <header class="masthead">
      <div class="brand">
        <span class="brand-mark"></span>
        <span class="brand-name">Harlan Defense, PLLC</span>
      </div>
      <address class="contact">
        P: (555) 410-2837<br>
        F: (555) 410-2838<br>
        PO Box 218 Millbrook, KY 40391
      </address>
    </header>

    <section class="letter-body">
      <p class="letter-date">Date, 10 September, 2020</p>
      <p>This is a sample letter that has been placed to demonstrate typing format (Your Company) letterhead design. When positioned properly, it will serve to work in harmony with all other elements letterhead. This letterhead design is meant to project an image of professionalism and reliability. By using simple alignment we have created a very spacious feeling. The simplicity suggests strength, and the spaciousness contributes to the aesthetics of the layout. These basic qualities along with the (Your Company) look and help reinforce the (Your Company) brand. When positioned properly, it will serve to work in harmony with all the other elements of the design, meant to project an image of professionalism and reliability.</p>
      <p>This letterhead design is based on the (Form of your logo) form (Your Company) logo. Each stationery piece has a very spacious feeling. The simplicity suggests strength; the spaciousness contributes as part of the (Form of your logo).</p>
    </section>

    <footer class="sign-off">
      <div class="signature" role="img" aria-label="Handwritten signature of Daniel Marsh"></div>
      <p>Daniel Marsh</p>
      <p>Manager</p>
    </footer>
  </article>
</body>
</html>
```